Porchlight To Bin Co Valet Trash Recycling

I want to create a colorful brochure, I really like my company colors, with basic information about valet trash for apartment complexes. You can include some apartment recycling information as well, but 80% trash, 20% recycling. I have included my logo in the attachments. Also, you can find information at porchlighttobinco.example, very basic and I will be redoing my website as well.

many people are giving information about business and residential recycling, I only want information on trash and recycling valet for apartments

Target Market(s)

apartment complex tenants and management

Industry/Entity Type

Apartment

Number of Pages Required

4 page

Font styles to use
Serif
Sans Serif

Colors
9bcb3b
f37122
0355a3

Requirements
Must have
• Tri-Fold brochure, colorful, well organized. Advantages for tenants and for property management.

```html
<!DOCTYPE html>
<html lang="en">
<head>
<meta charset="utf-8">
<title>Porchlight To Bin Co – Valet Trash Brochure</title>
<link href="https://fonts.googleapis.com/css2?family=Oswald:wght@500;700&family=Open+Sans:ital,wght@0,400;0,600;0,700;1,700&display=swap" rel="stylesheet">
<style>
:root{
  --blue:#0355a3;
  --blue-dark:#023c78;
  --orange:#f37122;
  --green:#9bcb3b;
  --paper:#f4f4f4;
  --ink:#222;
  --stage:#3a3a3a;
}
*{box-sizing:border-box;margin:0;padding:0}
html,body{width:833px;height:1200px;overflow:hidden}
body{background:var(--stage);font-family:"Open Sans",Arial,sans-serif;color:var(--ink);position:relative}
.spread{position:absolute;left:10px;width:813px;height:580px;display:flex;overflow:hidden;box-shadow:0 4px 14px rgba(0,0,0,.5)}
.spread--outside{top:12px}
.spread--inside{top:608px}
.panel{position:relative;width:271px;height:580px;overflow:hidden}
.panel--blue{background:var(--blue);color:#fff}
.panel--paper{background:linear-gradient(90deg,#e6e6e6,#fafafa 40%,#fff)}
h2{font-family:"Oswald",sans-serif;font-weight:700;font-size:13px;color:var(--orange);text-transform:uppercase;letter-spacing:.2px;margin-bottom:4px}
p{font-size:8.3px;line-height:1.32;margin-bottom:4px;text-align:justify}
.photo{position:absolute}
.brand{display:flex;align-items:center;gap:6px;font-family:"Open Sans",sans-serif;font-weight:600;color:var(--blue);font-size:13px}
.brand__dot{width:12px;height:12px;border-radius:50%;background:var(--orange);flex:none}
.badge{position:absolute;border:2px solid #3a8a30;border-radius:4px;background:#fff}

/* outside – about panel */
.about__photo{left:0;top:0;width:271px;height:170px;background:linear-gradient(135deg,#c8d6e4,#2f6fb8 55%,#1d4f95)}
.about__body{position:absolute;left:18px;right:14px;top:198px}
.about__card{position:absolute;left:18px;right:14px;bottom:14px;background:#fff;border-radius:8px;padding:8px;text-align:center;color:#333;font-size:7.5px;line-height:1.3}
.about__card strong{display:block;color:var(--blue);font-size:8.5px;margin-bottom:2px}

/* outside – contact panel */
.contact{padding:110px 0 0 30px}
.contact .brand{position:absolute;top:118px;left:22px}
.contact__name{font-family:"Oswald",sans-serif;font-weight:700;font-size:21px;color:var(--blue);margin-top:42px}
.contact__phone{display:flex;align-items:center;gap:8px;font-family:"Oswald",sans-serif;font-weight:500;font-size:18px;color:var(--orange);margin:6px 0 12px}
.contact__line{font-size:10px;line-height:1.35;margin-bottom:10px}
.contact__partner{font-size:12px;color:#555;margin-top:14px}
.contact__badge{left:30px;top:376px;width:108px;height:76px}

/* outside – cover panel */
.cover{background:#fff}
.cover .brand{position:absolute;top:22px;left:26px}
.cover__lower{position:absolute;left:0;right:0;bottom:0;height:250px;background:var(--orange)}
.cover__photo{left:58px;top:88px;width:180px;height:180px;border-radius:50%;background:linear-gradient(180deg,#8a8f96,#6a5c50 55%,#3b4d6a);border:6px solid var(--green);box-shadow:0 0 0 5px var(--blue)}
.cover__city{position:absolute;top:292px;left:0;right:0;text-align:center;font-family:"Oswald",sans-serif;font-weight:700;font-size:24px;color:var(--green);transform:rotate(4deg)}
.cover__text{position:absolute;left:22px;right:20px;top:352px;color:#222;font-size:9px}
.cover__text em{font-weight:700}
.pill{position:absolute;left:24px;right:24px;bottom:26px;height:22px;border-radius:11px;background:#fff;color:#222;font-size:9px;font-weight:600;display:flex;align-items:center;justify-content:center}

/* inside – how it works */
.how__body{position:absolute;left:18px;right:16px;top:24px}
.how__photo{left:0;bottom:40px;width:271px;height:180px;background:linear-gradient(180deg,#7fae4a,#5f9436)}
.how__foot{position:absolute;left:0;right:0;bottom:0;height:40px;background:var(--orange);color:#fff;font-size:9px;font-weight:600;display:flex;align-items:center;justify-content:center}

/* inside – benefits */
.benefits{padding:20px 14px 0 18px}
.benefits h2{margin-top:2px}
.benefits ul{list-style:none;margin-bottom:10px}
.benefits li{position:relative;padding-left:10px;font-size:8.3px;line-height:1.3;margin-bottom:3.5px;color:#333}
.benefits li::before{content:"";position:absolute;left:0;top:3px;width:4px;height:4px;border-radius:50%;background:var(--blue)}
.benefits__badge{left:18px;top:452px;width:62px;height:40px}
.benefits__photo{left:118px;top:445px;width:100px;height:100px;border-radius:50%;background:linear-gradient(180deg,#9a7b5f,#c9a886 45%,#2f6fc4);border:4px solid var(--green)}

/* inside – factors */
.factors{background:#fff}
.factors__top{padding:20px 14px 0 16px}
.credit{display:block;margin:6px auto 6px;width:fit-content;white-space:nowrap;background:var(--green);color:#fff;font-family:"Oswald",sans-serif;font-size:6.5px;text-align:center;border-radius:6px;padding:1px 8px}
.factors__top p{color:#333;font-size:8.5px}
.factors__blue{position:absolute;left:0;right:0;bottom:0;height:300px;background:var(--blue);color:#fff;padding:30px 14px 0 16px}
.factors__blue .brand{color:#fff;justify-content:center;margin-bottom:12px}
.factors__blue ul{list-style:none;margin-bottom:8px}
.factors__blue li{position:relative;padding-left:10px;font-size:8.2px;line-height:1.3;margin-bottom:5px;text-align:justify}
.factors__blue li::before{content:"";position:absolute;left:0;top:3px;width:4px;height:4px;border-radius:50%;background:var(--green)}
.fees{width:100%;border-collapse:collapse;font-size:7.8px;margin-top:6px}
.fees th,.fees td{border:1px solid #fff;padding:2px 4px;text-align:left}
.fees th{background:var(--blue-dark);font-weight:600}
</style>
</head>
<body>

<section class="spread spread--outside">
  <div class="panel panel--blue about">
    <div class="photo about__photo" role="img" aria-label="Photo of a worker in a safety vest beside a blue recycling bin"></div>
    <svg width="271" height="200" style="position:absolute;left:0;top:0" aria-hidden="true">
      <path d="M0 150 Q140 200 271 40 L271 0 L271 60 Q160 215 0 172 Z" fill="#9bcb3b"/>
      <path d="M0 172 Q160 215 271 60 L271 80 Q170 230 0 186 Z" fill="#f37122"/>
    </svg>
    <div class="about__body">
      <h2>About the Company</h2>
      <p>Porchlight To Bin Co (PTB) is a Houston-based business created by Marcus Delaney, a Bayou City University student and professional mixed martial artist. Marcus previously owned and operated the successful trash removal service, Marcus's Haul-Away, while he was a high school student-athlete in Galveston. He has now founded a similar service in the Houston area.</p>
      <p>Marcus plans to keep PTB ahead of its competitors by focusing on customer satisfaction, technology, efficiency, and professionalism.</p>
      <p>PTB is fully ensured; proof of insurance will be provided upon request.</p>
      <p>Testimonials from former clients reveal so much about how a company operates and performs. We are happy to provide references upon request.</p>
      <h2 style="margin-top:8px">PTB Services</h2>
      <p>Porchlight To Bin Co (PTB) is a complete trash and recycling valet service designed to keep apartment complexes and its units clean, make complexes more environmentally friendly, and to keep tenants satisfied.</p>
    </div>
    <div class="about__card">
      <strong>Keeping Apartment Complexes Cleaner and Greener Across Houston.</strong>
      porchlighttobinco.example<br>hello@porchlighttobinco.example<br>555-014-2286
    </div>
  </div>

  <div class="panel panel--paper contact">
    <div class="brand"><span class="brand__dot"></span>Porchlight To Bin Co</div>
    <div class="contact__name">MARCUS DELANEY</div>
    <div class="contact__phone">
      <svg width="18" height="18" viewBox="0 0 18 18" aria-hidden="true"><rect width="18" height="18" rx="3" fill="#0355a3"/><path d="M6 4 L8 4 L9 7 L7.5 8 Q8.5 10.5 10 11 L11 9.5 L14 10.5 L14 12.5 Q12 14.5 8 12 Q4.5 9 5 5 Z" fill="#fff"/></svg>
      (555) 014-2286
    </div>
    <div class="contact__line">4820 Larkspur Ave #210<br>Bellaire, TX 77401</div>
    <div class="contact__line">hello@porchlighttobinco.example</div>
    <div class="contact__line">www.porchlighttobinco.example</div>
    <div class="contact__partner">PTB is partnered with</div>
    <div class="badge contact__badge" role="img" aria-label="Partner badge"></div>
    <svg width="271" height="580" style="position:absolute;left:0;top:0;pointer-events:none" aria-hidden="true">
      <path d="M271 300 Q190 420 250 580 L271 580 Z" fill="#0355a3"/>
      <path d="M271 330 Q205 430 262 580 L271 580 Z" fill="#f37122"/>
    </svg>
  </div>

  <div class="panel cover">
    <div class="brand"><span class="brand__dot"></span>Porchlight To Bin Co</div>
    <div class="cover__lower"></div>
    <svg width="271" height="340" style="position:absolute;left:0;top:0" aria-hidden="true">
      <path id="cover-arc" d="M30 150 Q135 10 250 120" fill="none"/>
      <text font-family="Oswald, sans-serif" font-weight="700" font-size="12" fill="#0355a3"><textPath href="#cover-arc" startOffset="4%">FULL-SERVICE WASTE REMOVAL AND RECYCLING</textPath></text>
      <path d="M0 330 Q40 330 58 200 L50 200 Q30 320 0 322 Z" fill="#0355a3"/>
      <path d="M271 330 Q230 330 245 200 L253 200 Q240 320 271 322 Z" fill="#0355a3"/>
    </svg>
    <div class="photo cover__photo" role="img" aria-label="Photo of a smiling man carrying a trash bag outdoors"></div>
    <div class="cover__city">HOUSTON, TEXAS</div>
    <div class="cover__text"><p>Taking out somebody's trash is a timeless gesture of kindness. Porchlight To Bin Co (PTB) takes that act of kindness one step further: <em>your tenants will never again have to bother with trash past their own doorsteps!</em></p></div>
    <div class="pill">www.porchlighttobinco.example</div>
  </div>
</section>

<section class="spread spread--inside">
  <div class="panel panel--blue how">
    <div class="how__body">
      <h2>How Does It Work?</h2>
      <p>Uniformed PTB employees walk the property 5 nights a week (Sunday-Thursday) collecting bags of trash and bags of recyclables. They gather the bags from every PTB trashcan placed outside a door, as well as the litter on sidewalks, in parking lots, and around dumpster areas. Then the refuse is transported to dumpsters located on the property. If the nearest dumpster is at capacity, the refuse will be taken to the next available dumpster for disposal, ensuring that no dumpster will be overfilled, avoiding animal infestation.</p>
      <p>PTB's commitment to recycling sets it apart from other trash collection companies. PTB partners with Greenway Waste Services for their years of experience and streamlined services. With Greenway Waste Services it's easy for tenants to recycle. Tenants simply place recyclable items (paper, cardboard, glass, plastic, aluminum) into a marked bag and PTB, along with Greenway Waste Services, does the rest - collecting, separating, transporting, and recycling.</p>
    </div>
    <div class="photo how__photo" role="img" aria-label="Image area for a recycling-themed nature picture"></div>
    <div class="how__foot">www.porchlighttobinco.example</div>
  </div>

  <div class="panel panel--paper benefits">
    <h2>Benefits for Complex Tenants</h2>
    <ul>
      <li>Trash disposal is easy, safe, and convenient.</li>
      <li>Recycling is easy and convenient.</li>
      <li>Tenants will not have to deal with handling their garbage past their own doorsteps.</li>
      <li>No more scary, late night trips to the dumpster.</li>
      <li>Fewer rodent and/or bug infestations.</li>
      <li>Fewer foul smells inside and outside the apartment units.</li>
    </ul>
    <h2>Benefits for Complex Managers</h2>
    <ul>
      <li>Attracts new tenants with a unique amenity provided at no additional cost to complex owners and management.</li>
      <li>Allows maintenance crew to focus on maintenance calls and not trash complaints.</li>
      <li>Prevents rodent and/or bug infestations.</li>
      <li>Prevents damage in units caused by garbage buildup.</li>
      <li>Keeps apartment grounds and dumpsters cleaner.</li>
      <li>Provides another set of eyes and ears for security purposes.</li>
    </ul>
    <svg width="271" height="580" style="position:absolute;left:0;top:0;pointer-events:none" aria-hidden="true">
      <path d="M100 580 Q200 520 271 390 L271 420 Q215 530 140 580 Z" fill="#9bcb3b"/>
      <path d="M140 580 Q215 530 271 420 L271 580 Z" fill="#f37122"/>
    </svg>
    <div class="badge benefits__badge" role="img" aria-label="Partner badge"></div>
    <div class="photo benefits__photo" role="img" aria-label="Photo of a smiling child holding a blue recycling bin"></div>
  </div>

  <div class="panel factors">
    <div class="factors__top">
      <h2>Factors That Guide Potential Tenants</h2>
      <svg width="240" height="118" viewBox="0 0 240 118" aria-label="Pie chart of tenant decision factors" role="img">
        <g transform="translate(120 58)">
          <path d="M0 0 L0 -42 A55 42 0 0 1 54 8 Z" fill="#3f78bf"/>
          <path d="M0 0 L54 8 A55 42 0 0 1 -14 41 Z" fill="#7aa6d8"/>
          <path d="M0 0 L-14 41 A55 42 0 0 1 -54 -8 Z" fill="#a9c6e6"/>
          <path d="M0 0 L-54 -8 A55 42 0 0 1 -14 -40 Z" fill="#f3ef9a"/>
          <path d="M0 0 L-14 -40 A55 42 0 0 1 0 -42 Z" fill="#5c8fcb"/>
        </g>
        <g font-size="5.5" fill="#555" font-family="Open Sans, sans-serif">
          <text x="108" y="8">Amenities 6%</text>
          <text x="180" y="36">Curb Appeal 28%</text>
          <text x="168" y="104">Common Areas 26%</text>
          <text x="6" y="92">Security/Parking 22%</text>
          <text x="10" y="30">Unit Appeal 18%</text>
        </g>
      </svg>
      <span class="credit">COURTESY OF DANA WHITFIELD - APARTMENT MARKETING SPECIALIST</span>
      <p>Porchlight To Bin Co (PTB) helps properties improve in each of these areas which leads to higher occupancy rates, more satisfied tenants, and more lease renewals.</p>
    </div>
    <svg width="271" height="70" style="position:absolute;left:0;top:262px" aria-hidden="true">
      <path d="M0 70 Q120 0 271 30 L271 70 Z" fill="#0355a3"/>
      <path d="M0 60 Q110 -4 220 14" stroke="#9bcb3b" stroke-width="4" fill="none"/>
    </svg>
    <div class="factors__blue">
      <div class="brand"><span class="brand__dot"></span>Porchlight To Bin Co</div>
      <ul>
        <li>Your complex will stand out from the competition with this convenient amenity, a cleaner complex and cleaner apartment units.</li>
        <li>PTB's nighttime pick-ups mean extra security for complexes. Uniformed employees walking the grounds provide extra eyes and ears for the area.</li>
      </ul>
      <p>PTB fees are added to the tenants' current monthly trash and dumpster fees. PTB invoices management and is paid by the 10th day of each month, for the current month of service being provided.</p>
      <table class="fees">
        <tr><th>Valet Trash</th><th>Valet Trash &amp; Recycling</th></tr>
        <tr><td>3 days/week - $10/month</td><td>3 days/week - $20/month</td></tr>
        <tr><td>5 days/week - $15/month</td><td>5 days/week - $25/month</td></tr>
      </table>
    </div>
  </div>
</section>

</body>
</html>
```